New Cutting Edge Mood Supplement Needs Logo and Label Design

We need a logo and label design for our new supplement, BrivaLune. BrivaLune is a supplement designed by Halberg Nutraceuticals to help those suffering from feelings of depression that often come with a lack of sunlight related to vitamin D deficiency. BrivaLune increases energy, vitality, and improves overall mood. The final design should communicate positive energy and vitality in a modern, trustworthy way. If you can find a way to highlight both the 5000iu of vitamin D and the Calvera Blend Matrix (St John's Wort, 5-HTP, SAMe, and Ginkgo) that'd be ideal. Also, we're not tied to the "BrivaLune" form. We're open to any presentation of the word (ex: brivalune, BRIVALUNE, brivaLUNE, etc.)

Target Market(s)

Adults experiencing vitamin D deficiency with associated depression and/or seasonal depression

Industry/Entity Type

Supplement

Requirements
Nice to have
• We seem to be leaning towards blues, greens, and bright yellows. Please no oranges or dark/burnt yellows

```html
<!DOCTYPE html>
<html lang="en">
<head>
<meta charset="utf-8">
<title>BrivaLune Label</title>
<link rel="stylesheet" href="https://fonts.googleapis.com/css2?family=Anton&family=Archivo+Black&family=Oswald:wght@500;600&family=Arimo:wght@400;700&display=swap">
<style>
  :root {
    --ink: #111111;
    --lime: #7ed321;
    --lime-dark: #3f8a0c;
    --stage: #5c9e0f;
    --sun-core: #fff6a8;
    --sun-mid: #ffd43a;
    --sun-edge: #f59a16;
    --paper: #ffffff;
  }
  * { box-sizing: border-box; margin: 0; padding: 0; }
  html, body { width: 1200px; height: 1200px; overflow: hidden; }
  body { background: var(--stage); font-family: "Arimo", Arial, sans-serif; color: var(--ink); position: relative; }

  .label {
    position: absolute; left: 30px; top: 333px; width: 1140px; height: 534px; overflow: hidden;
    background:
      radial-gradient(ellipse 48% 70% at 50% 28%, var(--sun-core) 0%, var(--sun-mid) 45%, rgba(255,212,58,0) 80%),
      linear-gradient(90deg, var(--sun-edge) 0%, #ffbf2a 20%, #ffc92f 50%, #ffbf2a 80%, var(--sun-edge) 100%);
  }
  .label__top { position: absolute; left: 0; top: 0; width: 100%; height: 8px; background: var(--ink); }
  .label__top::after { content: ""; position: absolute; left: 0; top: 8px; width: 100%; height: 6px; background: linear-gradient(180deg, rgba(126,211,33,.8), rgba(126,211,33,0)); }
  .label__bottom { position: absolute; left: 0; bottom: 0; width: 100%; height: 30px;
    background: linear-gradient(90deg, var(--lime-dark) 0%, var(--ink) 25%, var(--ink) 75%, var(--lime-dark) 100%); }
  .label__bottom::before { content: ""; position: absolute; left: 0; top: -10px; width: 100%; height: 10px; background: linear-gradient(0deg, rgba(126,211,33,.9), rgba(126,211,33,0)); }

  .brand { font-family: "Anton", Impact, sans-serif; color: var(--ink); line-height: 1; letter-spacing: 0.5px; }
  .subhead { font-family: "Archivo Black", Arial, sans-serif; font-size: 9px; text-transform: uppercase; letter-spacing: .2px; }

  /* left panel */
  .side-panel { position: absolute; left: 57px; top: 46px; width: 230px; }
  .side-panel .brand { font-size: 47px; }
  .side-panel .subhead { margin: 6px 0 0 24px; }
  .copy { position: absolute; left: 86px; width: 176px; font-size: 8.4px; line-height: 1.15; }
  .copy h4 { font-size: 8.4px; font-weight: 700; text-transform: uppercase; }
  .copy--intro { top: 116px; }
  .copy--use { top: 178px; }
  .copy--warn { top: 252px; }
  .notices { position: absolute; left: 80px; top: 326px; font-family: "Archivo Black", Arial, sans-serif; font-size: 7.6px; text-transform: uppercase; }
  .notices li { list-style: none; margin-bottom: 6px; }
  .notices li::before { content: "• "; }
  .notices .notices__alert { background: var(--ink); color: var(--lime); padding: 2px 5px; display: inline-block; }
  .disclaimer { position: absolute; left: 72px; top: 382px; width: 194px; border: 1px solid var(--ink); padding: 3px 5px; font-size: 7.6px; line-height: 1.15; }
  .trust-row { position: absolute; left: 76px; top: 447px; display: flex; gap: 44px; align-items: center; }
  .trust-row .mark { width: 28px; height: 26px; background: var(--ink); border-radius: 3px; opacity: .85; }
  .trust-row .mark--round { border-radius: 50%; }
  .trust-row .mark--flag { width: 34px; height: 20px; background: #b03030; }

  /* front panel */
  .front { position: absolute; left: 0; top: 0; width: 100%; text-align: center; }
  .front__grade { position: absolute; left: 0; width: 1140px; top: 30px; font-family: "Archivo Black", Arial, sans-serif; font-size: 13px; letter-spacing: .3px; }
  .front__title { position: absolute; left: 0; width: 1140px; top: 47px; font-size: 70px; }
  .front__sub { position: absolute; left: 0; width: 1140px; top: 120px; font-size: 13px; }
  .hex-cluster { position: absolute; left: 340px; top: 130px; width: 460px; height: 280px; overflow: visible; }
  .hex-label { font-family: "Oswald", "Arial Narrow", sans-serif; font-weight: 600; fill: var(--ink); }
  .dietary { position: absolute; left: 608px; top: 345px; font-family: "Archivo Black", Arial, sans-serif; font-size: 14px; line-height: 1.05; text-align: left; }
  .claims { position: absolute; left: 494px; top: 428px; display: flex; gap: 15px; }
  .claims span { width: 40px; height: 40px; border-radius: 50%; border: 3px solid var(--ink); background: #ffd23b; display: block; }
  .count { position: absolute; left: 539px; top: 486px; width: 57px; height: 48px; background: var(--ink); color: var(--lime); text-align: center; font-family: "Archivo Black", Arial, sans-serif; z-index: 2; }
  .count b { display: block; font-size: 21px; line-height: 26px; font-weight: 400; }
  .count small { display: block; font-size: 9px; line-height: 10px; }

  /* facts panel */
  .facts { position: absolute; left: 874px; top: 57px; width: 203px; border: 2px solid var(--ink); padding: 2px 3px 4px; font-size: 6.6px; line-height: 1.25; }
  .facts h3 { font-family: "Archivo Black", Arial, sans-serif; font-size: 15px; font-weight: 400; line-height: 1.1; }
  .facts .rule-thick { border-top: 4px solid var(--ink); margin: 3px 0 2px; }
  .facts .rule-mid { border-top: 2px solid var(--ink); margin: 1px 0; }
  .facts .row { display: flex; border-bottom: 1px solid var(--ink); padding: 1px 0; }
  .facts .row span:first-child { flex: 1; }
  .facts .row span:nth-child(2) { width: 34px; text-align: right; }
  .facts .row span:nth-child(3) { width: 28px; text-align: right; }
  .facts .row--head { font-size: 6px; border-bottom: none; text-align: right; }
  .facts .row--bold { font-weight: 700; }
  .facts-notes { position: absolute; left: 874px; top: 297px; width: 203px; font-size: 6.8px; line-height: 1.2; }
  .facts-notes p { margin-bottom: 8px; }
  .facts-notes hr { border: none; border-top: 2px solid var(--ink); margin: 2px 0 4px; }
  .maker { position: absolute; left: 874px; top: 374px; width: 203px; text-align: center; font-size: 7px; line-height: 1.15; }
  .cert { position: absolute; left: 960px; top: 400px; width: 46px; height: 52px; background: #2a2a2a; clip-path: polygon(0 0, 100% 0, 100% 65%, 50% 100%, 0 65%); }
  .site { position: absolute; left: 874px; top: 476px; width: 215px; text-align: center; font-family: "Archivo Black", Arial, sans-serif; font-size: 13.5px; }
</style>
</head>
<body>
<main class="label">
  <div class="label__top"></div>

  <section class="side-panel">
    <div class="brand">BRIVALUNE</div>
    <div class="subhead">Vitamin D &amp; Calvera Blend Matrix</div>
  </section>
  <p class="copy copy--intro">Is a scientifically formulated vitamin D and mood support supplement comprised of clinically-tested ingredients with antidepressive properties.</p>
  <div class="copy copy--use"><h4>Sugested use:</h4>As a dietary supplement for adults, take as recommended by your health care professional or one serving of two (2) capsules daily. For best results, take in the morning. Use only as directed.</div>
  <div class="copy copy--warn"><h4>Warning:</h4>Do not exceed recommended serving size. If you are pregnant, nursing, or taking any medications, consult your doctor before use. Discontinue use and consult your doctor if any adverse reactions occur.</div>
  <ul class="notices">
    <li><span class="notices__alert">Keep out of reach children.</span></li>
    <li>Store in a dry place</li>
    <li>Avoid excessive heat.</li>
  </ul>
  <p class="disclaimer">**These statements have not been evaluated by the Food and Drug Administration. This product is not intended to diagnose, trat, cure or prevent any disease.</p>
  <div class="trust-row">
    <span class="mark mark--round" role="img" aria-label="Recycling badge"></span>
    <span class="mark" role="img" aria-label="Registered facility badge"></span>
    <span class="mark mark--flag" role="img" aria-label="Made in country badge"></span>
  </div>

  <section class="front">
    <div class="front__grade">PHARMACEUTICAL GRADE</div>
    <div class="front__title brand">BRIVALUNE</div>
    <div class="front__sub subhead">Vitamin D &amp; Calvera Blend Matrix</div>
  </section>

  <svg class="hex-cluster" viewBox="0 0 460 280" aria-label="Ingredient hexagons">
    <defs>
      <polygon id="hex" points="54,0 27,47 -27,47 -54,0 -27,-47 27,-47"/>
    </defs>
    <g stroke="#1a1a1a" stroke-width="2">
      <g transform="translate(161,109) rotate(-12)" role="img" aria-label="St. John's Wort flower illustration"><use href="#hex" fill="#8fe02c"/></g>
      <g transform="translate(273,120) rotate(-12)" role="img" aria-label="Ginkgo leaf illustration"><use href="#hex" fill="#8fe02c"/></g>
      <g transform="translate(359,55) rotate(-12)"><use href="#hex" fill="#8fe02c"/></g>
      <g transform="translate(389,163) rotate(-12)" role="img" aria-label="Coconut illustration"><use href="#hex" fill="#8fe02c"/></g>
      <g transform="translate(78,192) rotate(-12)"><use href="#hex" fill="#8fe02c"/></g>
      <g transform="translate(188,210) rotate(-12)" role="img" aria-label="Green tea leaves illustration"><use href="#hex" fill="#8fe02c"/></g>
    </g>
    <g class="hex-label">
      <text x="122" y="104" font-size="17" transform="rotate(-12 161 109)">St.Johns Wort</text>
      <text x="255" y="112" font-size="17" transform="rotate(-12 273 120)">Ginko</text>
      <text x="334" y="62" font-size="19" transform="rotate(-12 359 55)">5-HTP</text>
      <text x="360" y="158" font-size="17" transform="rotate(-12 389 163)">coconut</text>
      <text x="48" y="198" font-size="19" transform="rotate(-12 78 192)">SAM-e</text>
      <text x="156" y="200" font-size="17" transform="rotate(-12 188 210)">green tea</text>
    </g>
    <g fill="#111">
      <rect x="344" y="22" width="30" height="6" transform="rotate(-12 359 25)"/>
      <rect x="380" y="60" width="6" height="28" transform="rotate(18 383 74)"/>
      <rect x="54" y="210" width="6" height="28" transform="rotate(-40 57 224)"/>
      <rect x="100" y="188" width="6" height="28" transform="rotate(18 103 202)"/>
    </g>
  </svg>
  <div class="dietary">*Dietary<br>Supplement</div>
  <div class="claims">
    <span role="img" aria-label="Vegetarian badge"></span>
    <span role="img" aria-label="Sugar free badge"></span>
    <span role="img" aria-label="Dairy free badge"></span>
  </div>
  <div class="count"><b>90</b><small>capsules</small></div>

  <section class="facts">
    <h3>Supplement Facts</h3>
    <div>Serving Size: 2 capsules<br>Serving Per Container: 30 servings</div>
    <div class="rule-thick"></div>
    <div class="row row--head"><span></span><span>Amount per Serving</span><span>%Daily Value</span></div>
    <div class="rule-mid"></div>
    <div class="row"><span>Vitamin D3 (as Cholecalciferol)</span><span>5000 iu</span><span>1250%</span></div>
    <div class="row"><span>Vitamin B6 (as Pyridoxine HCl)</span><span>50 mg</span><span>2500%</span></div>
    <div class="row"><span>Folate (Folic Acid)</span><span>500 mcg</span><span>125%</span></div>
    <div class="row"><span>Vitamin B12 (as Cyanocobalamin)</span><span>500 mcg</span><span>8333%</span></div>
    <div class="rule-mid"></div>
    <div class="row row--bold"><span>Proprietary Blend 581 mg</span></div>
    <div class="row"><span>Green Tea (Camelia Sinensis-Leaf)</span></div>
    <div class="row"><span>St. Johns Wort (Aerial parts)</span></div>
    <div class="row"><span>Coconut Oil</span></div>
    <div class="row"><span>5-HTP (5-Hydroxytryptophan)</span></div>
    <div class="row"><span>Ginkgo (leaf)</span></div>
    <div class="row" style="border-bottom:none"><span>SAMe (S-Adenosyl-L-Methionine)</span></div>
  </section>
  <div class="facts-notes">
    <p><b>Daily Value:</b> Not Established</p>
    <hr>
    <p><b>Other Ingredients:</b> Gelatin Capsule, Cellulose, and Magnesium Stearate.</p>
    <p><b>Daily Value:</b> Not Established</p>
  </div>
  <div class="maker"><hr style="border:none;border-top:2px solid #111;margin-bottom:6px"><b>Formulated and Manufactured by:</b><br>Halberg Nutraceuticals</div>
  <div class="cert" role="img" aria-label="Quality certification badge"></div>
  <div class="site">www.brivalune.com</div>

  <div class="label__bottom"></div>
</main>
</body>
</html>
```